Tallow Ridge Index Website Design

NB! See updates below as well!
We need a website design for www.tallowridgeindex.co.za. The website is designed to drive traffic for businesses and consumers that want to go green.
The website serves two main purposes:
1. Provide a central repository of information provided by subject matter experts in various fields. These are called 'Ridge Notes'
2. Provide a directory of companies that can help you go green. A simple directory listing.
The site is a site for both business and consumers. Although our main target is business, consumers will drive up the traffic so the site is also designed this way.
The landing page needs to really ‘pop’ for the business and consumer sections on mouseover. Not sure to how to this but welcome suggestions. Sliding pictures and lots if imagery is welcomed.
Extensive advertising space is available which has been optimised for parlo adspring.
Although this is a website design, we have no logo so designs on logo's incorporated into the design are welcome and encouraged. The logo need to be extensible, in other words incorporate addition text for various sections like "Tallow Ridge Index for business", "Tallow Ridge Index for Consumers".
This is a green site so a green theme is a must, however, as there is also a business focus it needs to remain elegant and not go over the top with the green elements.
There are a number of page templates we need designed which are included in JPG format in the uploads section. These are not hard and fast designs but are there to provide an indication of what we require.
A website that we like that has a similar concept of merging a directory with content/information is www.vesmira.com.au.
We need the file format in PSD, the design chosen will be integrated with the directory theme at www.listforge.net so please bear this in mind with your design.
Updates
We have uploaded two more files that we have created in list forge, one is the business directory and the other is the listing section. As you can see the site functionality is all there, we just need it jazzed up and made unique.
We have noted that many projects get delayed constantly. We will choose a design tomorrow so get your designs in now. No time to wait.
Target Market(s)
Business and consumers, this is like two sites in one which makes it a bit tricky
Industry/Entity Type
Advertising
Requirements
Must have
- The landing page must clearly delineate between the business section and the consumer section. For example, if you are a business user you should be drawn to the business section immediately.
There must be areas for general content on the landing page to assist with SEO and we want a large footer to be used for links and general SEO optimisation.
We require a design for all 6 pages which will incorporate elements from all. Namely Landing Page, Business/Consumer Landing Page, Section Content Page (Datanook), Directory Catergory, Directory Listing, Contact Us/About Us
PSD format is welcome although CSS/HTML would be also welcomed.
Nice to have
- A logo for Tallow Ridge Index - must be extensible and include "Tallow Ridge Index for Business", " Tallow Ridge Index for Consumers", "Tallow Ridge Index directory"

```html
<!DOCTYPE html>
<html lang="en">
<head>
<meta charset="utf-8">
<title>Tallow Ridge Index</title>
<link rel="stylesheet" href="https://fonts.googleapis.com/css2?family=Open+Sans:wght@400;600;700&family=Arimo:wght@400;700&display=swap">
<style>
:root{
  --page:#dfe9d3;
  --frame:#c6d8b4;
  --white:#ffffff;
  --green:#6aa834;
  --green-dark:#4e8a22;
  --green-soft:#eef5e6;
  --text:#333333;
  --muted:#888888;
  --nav-text:#444444;
  --panel:#f4f4f4;
  --box-head:#e9ede6;
  --banner-dark:#123d12;
  --banner-mid:#3f7d33;
  --banner-light:#cfe8c2;
}
*{box-sizing:border-box;margin:0;padding:0}
html,body{width:1200px;height:854px;overflow:hidden}
body{background:var(--page);font-family:Arimo,Arial,sans-serif;color:var(--text);position:relative}
.site{position:absolute;left:12px;top:0;width:1178px;height:854px;background:var(--white);border-left:1px solid var(--frame);border-right:1px solid var(--frame);overflow:hidden}

.header{position:absolute;left:0;top:0;width:100%;height:91px;background:linear-gradient(#ffffff,#eef1ed)}
.brand{position:absolute;left:15px;top:17px;display:flex;align-items:center;gap:14px}
.brand-mark{width:53px;height:53px;border-radius:50%;background:var(--green)}
.brand-name{font-family:"Open Sans",sans-serif;font-size:30px;font-weight:400;color:var(--green)}
.search{position:absolute;left:922px;top:28px;width:194px;height:30px;border:1px solid #bbb;background:#fff;font-size:13px;padding:7px 5px;color:#333}
.search-icon{position:absolute;left:1125px;top:22px}
.header-rule{position:absolute;left:0;top:91px;width:100%;height:3px;background:var(--green);opacity:.6}
.nav{position:absolute;left:0;top:96px;width:100%;height:52px;background:linear-gradient(#f7f8f7,#dfe4e8);display:flex;align-items:center;padding-left:16px}
.nav a{font-family:Arimo,Arial,sans-serif;font-weight:700;font-size:15.5px;color:var(--nav-text);text-decoration:none;padding:0 20px 0 12px;border-right:1px solid #888;line-height:20px}
.nav a+a{padding-left:20px}
.banner{position:absolute;left:1px;top:150px;width:1176px;height:157px;background:linear-gradient(100deg,var(--banner-dark) 0%,var(--banner-mid) 40%,var(--banner-light) 75%,var(--banner-mid) 100%)}

.col-left{position:absolute;left:0;top:307px;width:234px;height:547px;background:#fbfbfb;border-right:2px solid #eee}
.col-right{position:absolute;left:940px;top:307px;width:238px;height:547px;background:var(--panel);border-left:3px solid #ddd}
.box{position:absolute;left:2px;width:228px;border:1px solid #e5e5e5;border-radius:8px;background:#fff}
.box-head{margin:6px 4px 0;height:46px;border-radius:10px;background:linear-gradient(#f6f7f5,var(--box-head));display:flex;align-items:center;gap:10px;padding-left:12px;font-family:Arimo,Arial,sans-serif;font-weight:700;font-size:17px;color:#444}
.dot{width:15px;height:15px;border-radius:50%;background:radial-gradient(circle at 40% 35%,#b8f08a,var(--green-dark));flex:none}

.notes{top:12px;height:159px}
.avatar{position:absolute;left:12px;top:59px;width:30px;height:30px;background:#c9c9c9;border-radius:3px}
.note-text{position:absolute;left:59px;top:102px;font-size:14px;white-space:nowrap}
.note-meta{position:absolute;left:48px;top:128px;font-size:11.5px;font-style:italic;white-space:nowrap}

.login{top:193px;height:230px;font-size:14px}
.login label{position:absolute;left:-2px;line-height:16px}
.field{position:absolute;left:-2px;width:127px;height:22px;border:1px solid #aaa;font-size:14px;padding:2px 3px;background:#fff}
.check{position:absolute;left:4px;top:146px;width:13px;height:13px;border:1px solid #666}
.btn{position:absolute;background:#e4e4e4;border:1px solid #999;font-size:14px;padding:2px 10px}
.login .link{position:absolute;left:-2px;color:var(--green);line-height:16px}

.directory{top:445px;height:120px}
.directory .field{left:8px;top:51px;width:194px;height:30px;padding:6px}

.content{position:absolute;left:257px;top:307px;width:670px;height:547px}
.crumb{position:absolute;top:19px;font-size:14px}
.page-title{position:absolute;top:44px;font-family:Arimo,Arial,sans-serif;font-weight:700;font-size:19px;color:var(--green);white-space:nowrap}
.article{position:absolute;left:20px}
.article-head{display:flex;align-items:flex-end;justify-content:space-between;border-bottom:4px solid #e3e3e3;padding-bottom:2px}
.article-title{font-family:Arimo,Arial,sans-serif;font-weight:700;font-size:17px;line-height:20px}
.icons{display:flex;gap:5px;padding-bottom:4px}
.icons svg{display:block}
.date{font-size:13px;color:var(--muted);margin-top:8px;line-height:17px}
.body-text{font-size:14px;margin-top:6px}
.updated{font-size:13px;color:var(--muted);margin-top:12px}

.sections{position:absolute;left:20px;top:346px;width:630px;display:flex;gap:14px}
.section-card{flex:1;height:92px;border:1px solid #d6e4c8;border-radius:8px;background:linear-gradient(#ffffff,var(--green-soft));padding:12px 14px}
.section-card h3{font-size:16px;font-weight:700;color:var(--green-dark);margin-bottom:6px}
.section-card p{font-size:13px;line-height:17px;color:#555}
.section-card .go{display:inline-block;margin-top:6px;font-size:12.5px;font-weight:700;color:var(--green)}

.footer{position:absolute;left:0;top:456px;width:670px;height:91px;background:#eef1ed;border-top:3px solid var(--green);padding:10px 20px;display:flex;gap:24px}
.footer-col h4{font-size:13px;font-weight:700;color:#444;margin-bottom:4px}
.footer-col a{display:block;font-size:12px;line-height:16px;color:#666;text-decoration:none}

.online{top:14px;height:58px}
.online p{position:absolute;left:-3px;top:56px;font-size:14px;white-space:nowrap}
</style>
</head>
<body>
<div class="site">
  <header class="header">
    <div class="brand"><span class="brand-mark"></span><span class="brand-name">Tallow Ridge Index</span></div>
    <div class="search">search...</div>
    <svg class="search-icon" width="40" height="40" viewBox="0 0 40 40" aria-hidden="true">
      <circle cx="16" cy="15" r="11" fill="#f2f4f5" stroke="#9aa2a8" stroke-width="3"/>
      <line x1="24" y1="23" x2="35" y2="34" stroke="#8a9298" stroke-width="5" stroke-linecap="round"/>
    </svg>
  </header>
  <div class="header-rule"></div>
  <nav class="nav"><a>Home</a><a>Ridge Note</a><a>Contact Us</a></nav>
  <div class="banner" role="img" aria-label="Banner image: glowing green globe with light streaks"></div>

  <aside class="col-left">
    <section class="box notes">
      <div class="box-head"><span class="dot"></span>Latest Ridge Notes</div>
      <div class="avatar"></div>
      <p class="note-text">This is a sample microblog...</p>
      <p class="note-meta">682 days ago | Points:0</p>
    </section>
    <section class="box login">
      <div class="box-head"><span class="dot"></span>Login or Register</div>
      <label style="top:51px">Username</label>
      <div class="field" style="top:68px">lvarkov</div>
      <label style="top:95px">Password</label>
      <div class="field" style="top:112px">••••••••</div>
      <span class="check"></span>
      <label style="left:24px;top:145px">Remember me</label>
      <span class="btn" style="left:-2px;top:163px">Login</span>
      <span class="link" style="top:193px">Forgot login?</span>
      <span class="link" style="top:211px">Register</span>
    </section>
    <section class="box directory">
      <div class="box-head"><span class="dot"></span>Search Directory</div>
      <div class="field">Search...</div>
      <span class="btn" style="left:8px;top:83px">Search</span>
    </section>
  </aside>

  <main class="content">
    <p class="crumb">Home</p>
    <h1 class="page-title">Welcome to the Frontpage</h1>
    <article class="article" style="top:84px;width:306px">
      <div class="article-head">
        <h2 class="article-title">Tallow Ridge Index</h2>
        <div class="icons">
          <svg width="14" height="16" aria-hidden="true"><rect x="1" y="1" width="12" height="14" fill="#fff" stroke="#c33"/><rect x="3" y="6" width="8" height="4" fill="#c33"/></svg>
          <svg width="18" height="16" aria-hidden="true"><rect x="4" y="1" width="10" height="5" fill="#fff" stroke="#777"/><rect x="1" y="6" width="16" height="6" fill="#999"/><rect x="4" y="10" width="10" height="5" fill="#fff" stroke="#777"/></svg>
          <svg width="18" height="14" aria-hidden="true"><rect x="1" y="2" width="16" height="10" fill="#dde8f4" stroke="#36c"/><path d="M1 2 L9 8 L17 2" fill="none" stroke="#36c"/></svg>
        </div>
      </div>
      <p class="date">Tuesday, 22 November 2011 22:48</p>
      <p class="body-text">This is only a test.</p>
      <p class="updated">Last Updated on Tuesday, 22 November 2011 22:49</p>
    </article>
    <article class="article" style="top:209px;width:164px">
      <div class="article-head">
        <h2 class="article-title">Lena<br>Varkov</h2>
        <div class="icons">
          <svg width="14" height="16" aria-hidden="true"><rect x="1" y="1" width="12" height="14" fill="#fff" stroke="#c33"/><rect x="3" y="6" width="8" height="4" fill="#c33"/></svg>
          <svg width="18" height="16" aria-hidden="true"><rect x="4" y="1" width="10" height="5" fill="#fff" stroke="#777"/><rect x="1" y="6" width="16" height="6" fill="#999"/><rect x="4" y="10" width="10" height="5" fill="#fff" stroke="#777"/></svg>
          <svg width="18" height="14" aria-hidden="true"><rect x="1" y="2" width="16" height="10" fill="#dde8f4" stroke="#36c"/><path d="M1 2 L9 8 L17 2" fill="none" stroke="#36c"/></svg>
        </div>
      </div>
      <p class="date">Tuesday, 22 November<br>2011 22:47</p>
      <p class="body-text">Lena Varkov</p>
    </article>

    <div class="sections">
      <section class="section-card">
        <h3>Tallow Ridge Index for Business</h3>
        <p>Ridge Notes, listings and green suppliers for your company.</p>
        <span class="go">Enter business section →</span>
      </section>
      <section class="section-card">
        <h3>Tallow Ridge Index for Consumers</h3>
        <p>Simple guides and local services to help your home go green.</p>
        <span class="go">Enter consumer section →</span>
      </section>
    </div>

    <footer class="footer">
      <div class="footer-col"><h4>Business</h4><a>Ridge Notes</a><a>Green suppliers</a><a>Advertise</a></div>
      <div class="footer-col"><h4>Consumers</h4><a>Home and garden</a><a>Energy saving</a><a>Recycling</a></div>
      <div class="footer-col"><h4>Directory</h4><a>Categories</a><a>Add a listing</a><a>Search</a></div>
      <div class="footer-col"><h4>About</h4><a>About us</a><a>Contact us</a><a>www.tallowridgeindex.co.za</a></div>
    </footer>
  </main>

  <aside class="col-right">
    <section class="box online">
      <div class="box-head" style="justify-content:center;padding-left:0"><span class="dot" style="margin-right:16px"></span>Who's Online</div>
      <p>We have 1 guest online</p>
    </section>
  </aside>
</div>
</body>
</html>
```